Flyer-Design für Immobilienhändler
Zielgruppe
Ich bin ein kleiner Immobilienhändler (nebenberuflich, meine Frau und ich, 2-Mann Unternehmen) und kaufe direkt Wohnimmobilen (Haus/Wohnungen) ein, um diese aufzuwerten und dann wieder zu verkaufen. Ich bin kein Makler, habe aber ähnliche Zielgruppen wie ein Makler, nur mit dem Unterschied das ich die Immos direkt kostenfrei kaufe so wie sie sind! Zielgruppe sind bei mir Privatpersonen (im mittlerem-höherem Alter 50-80 Jahre) die Ihre Immobilie verkaufen möchten.
Aufgabenstellung
Es soll ein Flyer sein mit folgenden Vorgaben:
• Design: Modern, einfach und wichtig ist das es professional und sehr seriös wirkt
• Auf den ersten Blick sollte die Message verständlich sein was ich suche und was die Vorteile sind es bei mir zu verkaufen, anstatt das einem Makler zu übergeben (siehe mein Entwurf).
• Flyer Format z.B. DIN A5/A6, was sich gut versenden lässt. Vorschläge sind willkommen
Im Anhang habe ein einen eigenen Entwurf beigefügt, jedoch bin offen für komplett neue Vorschläge was Text und Design angeht.

```html
<!DOCTYPE html>
<html lang="de">
<head>
<meta charset="utf-8">
<title>Hausweit – Flyer</title>
<link href="https://fonts.googleapis.com/css2?family=Montserrat:wght@400;600;700;800&display=swap" rel="stylesheet">
<style>
  :root {
    --brand-blue: #1d4f91;
    --brand-yellow: #fcc72a;
    --accent-orange: #f5b400;
    --paper: #ffffff;
    --backdrop: #eeeeee;
    --skyline-light: #e3ebf6;
    --skyline-deep: #c3d3ea;
  }
  * { box-sizing: border-box; margin: 0; padding: 0; }
  html, body { width: 1200px; height: 2890px; overflow: hidden; }
  body {
    background: var(--backdrop);
    font-family: "Montserrat", sans-serif;
    color: var(--brand-blue);
    position: relative;
  }
  .flyer {
    position: absolute;
    left: 63px;
    width: 1074px;
    height: 756px;
    background: var(--paper);
    box-shadow: 0 6px 18px rgba(0,0,0,.18);
    overflow: hidden;
  }
  .flyer--front { top: 640px; }
  .flyer--back { top: 1496px; }

  .bar-top { position: absolute; left: 0; top: 0; width: 409px; height: 17px; background: var(--brand-blue); }
  .bar-side { position: absolute; right: 0; width: 17px; background: var(--brand-yellow); }
  .flyer--front .bar-side { top: 563px; height: 193px; }
  .flyer--back .bar-side { top: 0; height: 168px; }

  .brand-box {
    position: absolute;
    z-index: 2;
    background: var(--brand-yellow);
    display: flex; align-items: center; justify-content: center;
    font-weight: 800; color: var(--brand-blue); letter-spacing: .5px;
  }
  .flyer--front .brand-box { left: 810px; top: 81px; width: 176px; height: 93px; font-size: 28px; }
  .flyer--back .brand-box { left: 77px; top: 412px; width: 165px; height: 88px; font-size: 26px; }

  .front-headline {
    position: absolute; right: 88px; top: 238px;
    text-align: right; font-weight: 800; font-size: 51px; line-height: 61px;
  }
  .front-benefits {
    position: absolute; right: 88px; top: 384px;
    text-align: right; color: var(--accent-orange); font-weight: 400; font-size: 31px; line-height: 37px;
  }
  .skyline {
    position: absolute;
    z-index: 1;
    background: linear-gradient(180deg, var(--skyline-light), var(--skyline-deep));
  }
  .flyer--front .skyline { left: 17px; top: 527px; width: 1036px; height: 229px; }
  .flyer--back .skyline { left: 17px; top: 512px; width: 535px; height: 244px; }

  .back-headline {
    position: absolute; left: 76px; top: 114px;
    font-weight: 800; font-size: 51px; line-height: 60px;
  }
  .section-title { font-weight: 700; font-size: 21px; margin-bottom: 10px; }
  .about { position: absolute; left: 77px; top: 210px; width: 410px; }
  .about p { font-size: 17.5px; line-height: 22px; }
  .about .signature { font-weight: 700; font-size: 18.5px; margin-top: 26px; }

  .reasons { position: absolute; left: 588px; top: 210px; width: 440px; }
  .reasons ul { list-style: none; }
  .reasons li { position: relative; font-size: 17.5px; line-height: 22px; margin-bottom: 21px; white-space: nowrap; }
  .reasons li svg { position: absolute; left: -44px; top: 3px; }

  .contact {
    position: absolute; right: 94px; top: 605px; text-align: right;
  }
  .contact h3 { font-weight: 700; font-size: 21px; line-height: 26px; margin-bottom: 10px; }
  .contact-line { font-size: 17.5px; line-height: 26px; display: flex; justify-content: flex-end; align-items: center; gap: 14px; }
  .contact-line svg { width: 20px; height: 20px; }
</style>
</head>
<body>

<section class="flyer flyer--front">
  <div class="bar-top"></div>
  <div class="brand-box">Hausweit</div>
  <h1 class="front-headline">Sie möchten Ihre Immobilie<br>zum Bestpreis verkaufen?</h1>
  <p class="front-benefits">Ohne Renovierung/Sanierung<br>Ohne Gebühren und Besucherstress</p>
  <div class="skyline" role="img" aria-label="Linienillustration einer Stadtsilhouette mit Häusern, Kirchturm, Bäumen und Fabrik"></div>
  <div class="bar-side"></div>
</section>

<section class="flyer flyer--back">
  <div class="bar-top"></div>
  <div class="bar-side"></div>
  <h2 class="back-headline">Wir kaufen Ihre Immobilie</h2>

  <div class="about">
    <h3 class="section-title">Wer sind wir?</h3>
    <p>Wir sind keine Makler. Wi sind kein<br>Familienunternehme das sich auf den<br>Immobilien ankauf im Rhein-Main Gebit<br>spezialisiert hat. Wir kaufe gute und solide<br>Immobilienz um Bestpreis, direkt.</p>
    <p class="signature">Dipl.-Bauing. Lukas Feldmann</p>
  </div>

  <div class="brand-box">Hausweit</div>
  <div class="skyline" role="img" aria-label="Linienillustration einer Häuserreihe mit Kirchturm"></div>

  <div class="reasons">
    <h3 class="section-title">Warum mit uns?</h3>
    <ul>
      <li><svg width="16" height="14" viewBox="0 0 16 14"><path d="M1 7l5 5L15 1" fill="none" stroke="#fcc72a" stroke-width="2.2"/></svg>Abkauf direkt von uns, zum fairen Bestpreis</li>
      <li><svg width="16" height="14" viewBox="0 0 16 14"><path d="M1 7l5 5L15 1" fill="none" stroke="#fcc72a" stroke-width="2.2"/></svg>Professionelle, schnelle und komplette<br>Kaufabwicklung aus einer Hand</li>
      <li><svg width="16" height="14" viewBox="0 0 16 14"><path d="M1 7l5 5L15 1" fill="none" stroke="#fcc72a" stroke-width="2.2"/></svg>Sie brauchen nicht renovieren, sanieren oder<br>entrümpeln</li>
      <li><svg width="16" height="14" viewBox="0 0 16 14"><path d="M1 7l5 5L15 1" fill="none" stroke="#fcc72a" stroke-width="2.2"/></svg>Keine Maklergebühr, kein Besucherstress</li>
      <li><svg width="16" height="14" viewBox="0 0 16 14"><path d="M1 7l5 5L15 1" fill="none" stroke="#fcc72a" stroke-width="2.2"/></svg>Kein Haftungsrisiko -Wir kaufen Ihre<br>Immobilie so wie sie ist</li>
    </ul>
  </div>

  <div class="contact">
    <h3>Sie möchten ein<br>unverbindliches Angebot?</h3>
    <div class="contact-line">lf@hausweit.net
      <svg viewBox="0 0 20 20"><rect x="1" y="4" width="18" height="13" rx="1.5" fill="#fcc72a"/><path d="M2 5l8 6 8-6" fill="none" stroke="#fff" stroke-width="1.6"/></svg>
    </div>
    <div class="contact-line">06021 / 48 37 15
      <svg viewBox="0 0 20 20"><path d="M5 2l3 4-2 2c1 2.5 3 4.5 5.5 5.5l2-2 4 3-2 3C9 17 3 11 2 4z" fill="#fcc72a"/></svg>
    </div>
  </div>
</section>

</body>
</html>
```